Kravin House Music DJ Chatterly Banner

Hi there,
This is for a house music dj Chatterly site. Looking for the top banner to replace my page. You can check put Kravin on Chatterly to see the banner.
The name Kravin is pronounced like Fossil. use Dinosaurs a lot in my music. The whole idea is because I an older DJ. A fossil. I need a cool banner I can also use on Chatterly and Blinkpost.

https://www.chatterlyhub.com/Kravin

Target Market(s)

Target market is people who enjoy house music, EDM, dance music, etc.

Industry/Entity Type

House

Font styles to use
Sans Serif

Requirements
Must have
• The banner must be modern and cool looking appealing to EDM music lovers
• Must be reflective of my "fossil" theme but use my dj name Kravin
Nice to have
• Dinosaur feel but not cartoony.
• Steel or fossil look
Should not have
• DO NOT say DJ KRAVIN. Only Kravin
• Do not use the uploads in the design. Looking for a new concept completely

```html
<!DOCTYPE html>
<html lang="en">
<head>
<meta charset="utf-8">
<title>Kravin – Chatterly Banner</title>
<link rel="stylesheet" href="https://fonts.googleapis.com/css2?family=Montserrat:wght@800&display=swap">
<style>
  :root {
    --sand-light: #d8cbbd;
    --sand-mid: #c4b4a3;
    --sand-dark: #a99885;
    --stone-face: #a89a8a;
    --stone-light: #cfc2b3;
    --stone-edge: #857767;
    --stone-side: #5f5348;
    --stone-shadow: rgba(50, 38, 28, 0.45);
  }
  html, body {
    margin: 0;
    padding: 0;
    width: 1200px;
    height: 444px;
    overflow: hidden;
    background: var(--sand-mid);
  }
  .banner {
    position: relative;
    width: 1200px;
    height: 444px;
    overflow: hidden;
  }
  .sand-ground {
    position: absolute;
    inset: 0;
    background:
      radial-gradient(ellipse at 55% 40%, var(--sand-light) 0%, var(--sand-mid) 55%, var(--sand-dark) 100%);
  }
  .wordmark {
    position: absolute;
    inset: 0;
  }
  .letters {
    font-family: 'Montserrat', 'Arial Black', sans-serif;
    font-weight: 800;
    font-size: 196px;
    letter-spacing: 6px;
  }
  .letters-shadow { fill: var(--stone-shadow); filter: url(#soft-shadow); }
  .letters-side { fill: var(--stone-side); }
  .letters-face {
    fill: url(#stone-face);
    stroke: var(--stone-edge);
    stroke-width: 3px;
    paint-order: stroke;
    filter: url(#stone-grain);
  }
  .letters-bevel {
    fill: none;
    stroke: var(--stone-light);
    stroke-width: 1.5px;
    opacity: 0.7;
  }
</style>
</head>
<body>
  <main class="banner">
    <div class="sand-ground" role="img" aria-label="Fine beige desert sand with faint footprints"></div>
    <svg class="wordmark" width="1200" height="444" viewBox="0 0 1200 444" role="img" aria-label="Kravin">
      <defs>
        <linearGradient id="stone-face" x1="0" y1="0" x2="0" y2="1">
          <stop offset="0" stop-color="#bfb1a1"/>
          <stop offset="0.55" stop-color="#a69888"/>
          <stop offset="1" stop-color="#8f8171"/>
        </linearGradient>
        <filter id="stone-grain" x="-5%" y="-5%" width="110%" height="110%">
          <feTurbulence type="fractalNoise" baseFrequency="0.9" numOctaves="3" seed="4" result="noise"/>
          <feColorMatrix in="noise" type="matrix"
            values="0 0 0 0 0.25  0 0 0 0 0.2  0 0 0 0 0.15  0 0 0 0.55 0" result="speckle"/>
          <feComposite in="speckle" in2="SourceGraphic" operator="in" result="grain"/>
          <feMerge>
            <feMergeNode in="SourceGraphic"/>
            <feMergeNode in="grain"/>
          </feMerge>
        </filter>
        <filter id="soft-shadow" x="-10%" y="-30%" width="120%" height="160%">
          <feGaussianBlur stdDeviation="7"/>
        </filter>
        <text id="kravin-word" class="letters" x="0" y="0" textLength="920" lengthAdjust="spacingAndGlyphs">KRAVIN</text>
      </defs>
      <g transform="translate(228 336) rotate(-10)">
        <use href="#kravin-word" class="letters-shadow" x="10" y="20"/>
        <use href="#kravin-word" class="letters-side" x="3" y="14"/>
        <use href="#kravin-word" class="letters-side" x="2" y="10"/>
        <use href="#kravin-word" class="letters-side" x="1" y="6"/>
        <use href="#kravin-word" class="letters-side" x="0" y="3"/>
        <use href="#kravin-word" class="letters-face"/>
        <use href="#kravin-word" class="letters-bevel" x="-1" y="-1"/>
      </g>
    </svg>
  </main>
</body>
</html>
```